FOOD DELIVERY BRAND NEEDS WEBSITE TO GET SUBSCRIBERS

web design needed for a food delivery brand/label,
website should display who we are, how it works and push futur clients to get the label for an online application. Should look serious/official, trustworthy and confident. colors are black and gold like logo

Target Market(s)

restaurants

Industry/Entity Type

restaurant

Number of Pages Required

4 page

Requirements
Must have
• home page, who we are, our partners, subscribe, 2 subscribe button : 1 on top 1 bottom
Nice to have
• a graphic showing average + 15% sales thanks the label

```html
<!DOCTYPE html>
<html lang="en">
<head>
<meta charset="utf-8">
<title>Gilded Plate Seal</title>
<link href="https://fonts.googleapis.com/css2?family=Lato:wght@400;700;900&family=Montserrat:wght@600;700;800&family=Playfair+Display:wght@500&display=swap" rel="stylesheet">
<style>
:root{
  --black:#000;
  --ink:#0d0d0d;
  --gold:#c9a75f;
  --gold-soft:#d2b36a;
  --gold-deep:#a47b2f;
  --gold-text:#c8a158;
  --white:#fff;
  --grey:#1b1b1b;
  --muted:#d9d9d9;
}
*{margin:0;padding:0;box-sizing:border-box}
html,body{width:1200px;height:3669px;overflow:hidden;background:var(--black)}
body{position:relative;font-family:'Lato',sans-serif;color:var(--white)}
.abs{position:absolute}
.layer{position:absolute;left:0;top:0;width:1200px;height:3669px}

/* header */
.hero-panel{left:891px;top:0;width:309px;height:616px;background:var(--gold)}
.nav a{position:absolute;top:48px;font-size:15px;color:var(--white);text-decoration:none;font-family:'Lato',sans-serif}
.nav a.active{color:var(--gold)}
.brand{text-align:center;font-family:'Montserrat',sans-serif;font-weight:700;color:var(--gold);letter-spacing:1px;line-height:1.1}
.brand .dot{display:block;margin:0 auto 6px;border-radius:50%;border:2px solid var(--gold)}
.btn{position:absolute;display:flex;align-items:center;justify-content:center;border-radius:40px;font-family:'Lato',sans-serif;font-size:16px}
.btn-dark{background:var(--black);color:var(--white)}
.btn-gold{background:var(--gold);color:var(--black)}
.btn-gold-text{background:var(--black);color:var(--gold)}

.hero-copy{left:140px;top:222px;width:434px;text-align:center}
.hero-copy .welcome{font-family:'Playfair Display',serif;font-size:28px;color:var(--white)}
.hero-copy .title{font-family:'Playfair Display',serif;font-size:46px;color:var(--gold);line-height:1.05}
.hero-copy .title .under{border-bottom:2px solid var(--white);padding-bottom:2px}
.hero-copy p{font-size:17px;line-height:24px;margin-top:18px}

.sales-bar{position:absolute;border-radius:40px;background:var(--gold-soft);display:flex;align-items:center}
.sales-bar .label{font-family:'Montserrat',sans-serif;font-weight:700;font-size:20px;color:var(--black)}

.phone{left:844px;top:118px;width:226px;height:454px;border-radius:30px;background:linear-gradient(160deg,#f4f4f4,#dcdcdc);box-shadow:0 0 40px rgba(80,80,140,.5)}

/* sections */
.section-title{position:absolute;left:0;width:1200px;text-align:center;font-family:'Montserrat',sans-serif;font-weight:700;font-size:32px;color:var(--gold-text);letter-spacing:.5px}
.rule{position:absolute;height:3px;width:48px;background:var(--gold)}

.who-title{left:652px;top:795px;font-family:'Montserrat',sans-serif;font-weight:700;font-size:31px;color:var(--gold-text)}
.who-copy{left:652px;top:866px;width:407px;font-size:13.5px;line-height:24px;text-align:justify;color:var(--muted)}
.who-copy p+p{margin-top:11px}

.photo{position:absolute;border-radius:50%}

.step-bar{left:158px;top:1469px;width:885px;height:47px;background:var(--grey)}
.step{position:absolute;width:200px;text-align:center}
.step h3{font-family:'Lato',sans-serif;font-weight:900;font-size:11.5px;margin-top:0}
.step p{font-size:10.5px;line-height:16px;margin-top:9px}

.member{position:absolute;width:284px;height:284px;border-radius:50%;background:var(--ink);border:2px solid #3a3a3a;text-align:center}
.member.featured{border:3px solid var(--gold)}
.member .name{margin-top:68px;font-family:'Lato',sans-serif;font-weight:700;font-size:34px;color:#8a8a8a;display:flex;align-items:center;justify-content:center;gap:8px}
.member .name i{display:inline-block;width:26px;height:26px;border-radius:50%;background:#8a8a8a}
.member p{font-size:15px;line-height:27px;margin-top:16px}
.badge-sales{left:627px;top:1951px;width:80px;height:62px;border-radius:0 0 40px 40px;background:var(--gold);color:var(--black);font-family:'Montserrat',sans-serif;font-weight:800;font-size:10px;line-height:11px;text-align:center;padding-top:20px}

.cta-copy{left:145px;top:2345px;width:425px;font-size:17px;line-height:27px;text-align:justify}

.news-title{left:0;top:2850px;width:1200px;text-align:center;font-family:'Montserrat',sans-serif;font-weight:700;font-size:57px;line-height:68px;color:var(--white)}
.news-copy{left:0;top:3012px;width:1200px;text-align:center;font-size:23px;color:var(--white)}
.email{left:320px;top:3092px;width:383px;height:47px;border-radius:30px;background:var(--white);color:#333;font-size:13px;padding-left:34px;display:flex;align-items:center}
.subscribe{left:712px;top:3092px;width:168px;height:47px;border-radius:30px;background:#2a2620;color:var(--gold);font-family:'Montserrat',sans-serif;font-weight:700;font-size:15px;display:flex;align-items:center;justify-content:center}

.foot-divider{position:absolute;top:3310px;width:2px;height:163px;background:var(--gold)}
.foot-divider::before{content:"";position:absolute;top:0;left:0;width:2px;height:18px;background:var(--gold)}
.foot-col{position:absolute;top:3305px}
.foot-col h4{font-family:'Lato',sans-serif;font-weight:700;font-size:19px;color:var(--white);margin-bottom:16px}
.foot-col a{display:block;color:var(--white);font-size:13.5px;text-decoration:none;line-height:26.5px}
.social{position:absolute;width:52px;height:52px;border-radius:50%;background:var(--gold)}
.foot-line{left:0;top:3530px;width:1200px;height:1px;background:#2a2a2a}
.copyright{left:158px;top:3572px;font-size:13px;color:var(--white)}
.store{position:absolute;top:3564px;width:111px;height:34px;border-radius:5px;background:#000;border:1.5px solid #bbb}
</style>
</head>
<body>

<!-- Header -->
<div class="abs hero-panel"></div>
<nav class="nav">
  <a class="active" style="left:118px">Home</a>
  <a style="left:192px">Who we are</a>
  <a style="left:299px">How it works</a>
  <a style="left:695px">Our Members</a>
  <a style="left:814px">Contact</a>
</nav>
<div class="abs brand" style="left:518px;top:22px;width:160px;font-size:15px">
  <span class="dot" style="width:44px;height:44px"></span>GILDED PLATE<br><span style="font-size:12px">SEAL</span>
</div>
<a class="btn btn-dark" style="left:922px;top:36px;width:157px;height:42px;font-size:17px">Subscribe Now</a>

<!-- Hero -->
<svg class="layer" aria-hidden="true">
  <path d="M 760 410 A 190 190 0 0 1 900 190" fill="none" stroke="var(--gold)" stroke-width="5"/>
  <path d="M 732 410 A 190 190 0 0 0 900 545" fill="none" stroke="var(--gold)" stroke-width="5"/>
  <circle cx="727" cy="344" r="36" fill="none" stroke="var(--gold)" stroke-width="4"/>
  <path d="M 808 414 H 860 M 852 408 L 860 414 L 852 420" fill="none" stroke="#ddd" stroke-width="2"/>
  <path d="M 1060 404 H 1012 M 1020 398 L 1012 404 L 1020 410" fill="none" stroke="#222" stroke-width="2"/>
</svg>
<div class="abs phone" role="img" aria-label="Phone showing a restaurant listing app with food photos and ratings"></div>

<div class="abs hero-copy">
  <div class="welcome">Welcome to</div>
  <div class="title">Gilded <span class="under">Plate</span><br>Seal</div>
  <p>Lorem ipsum dolor sit amet, consectetur adipiscing<br>elit, sed do eiusmod tempor incididun.</p>
</div>
<a class="btn btn-gold" style="left:280px;top:428px;width:157px;height:40px">Subscribe Now</a>

<div class="sales-bar" style="left:121px;top:538px;width:656px;height:78px">
  <span class="label" style="margin-left:46px">AVERAGE 15% ONLINE SALES</span>
</div>
<a class="btn btn-gold-text" style="left:584px;top:557px;width:158px;height:42px">Subscribe Now</a>

<!-- Who we are -->
<svg class="layer" aria-hidden="true">
  <circle cx="319" cy="957" r="197" fill="none" stroke="var(--gold)" stroke-width="6"/>
  <circle cx="454" cy="1090" r="64" fill="var(--gold)"/>
</svg>
<div class="photo" style="left:131px;top:769px;width:376px;height:376px;background:radial-gradient(circle at 45% 40%,#e9e3dc,#c7b8a8 60%,#8d7a68)" role="img" aria-label="Smiling woman at a kitchen table looking at her phone over a salad"></div>
<div class="photo" style="left:396px;top:1032px;width:116px;height:116px;background:var(--black);border:3px solid var(--gold)"></div>
<div class="abs brand" style="left:404px;top:1063px;width:100px;font-size:10px">
  <span class="dot" style="width:22px;height:22px"></span>GILDED PLATE<br>SEAL
</div>

<div class="abs who-title">WHO WE ARE</div>
<div class="rule" style="left:716px;top:842px;width:60px"></div>
<div class="abs who-copy">
  <p>Lorem ipsum dolor sit amet consectetur adipiscing elit, sed do eiusmod tempor incididunt ut labore et dolore magna aliqua. Ut enim ad minim veniam, quis nostrud exercitation ullamco laboris nisi ut aliquip ex ea commodo consequat. Duis aute irure dolor in reprehenderit in voluptate velit essea.</p>
  <p>Lorem ipsum dolor sit amet consectetur adipiscing elit, sed do eiusmod tempor incididunt ut labore et dolore magna aliqua. Ut enim ad minim veniam quis nostrud.</p>
</div>

<!-- How it works -->
<div class="section-title" style="top:1247px">HOW IT WORKS</div>
<div class="rule" style="left:576px;top:1304px"></div>

<div class="abs step-bar"></div>
<svg class="layer" aria-hidden="true">
  <g fill="none" stroke="var(--gold)" stroke-width="3">
    <path d="M 152 1502 A 118 118 0 0 0 388 1502"/>
    <path d="M 378 1482 A 118 118 0 0 1 614 1482"/>
    <path d="M 590 1502 A 118 118 0 0 0 826 1502"/>
    <path d="M 818 1482 A 118 118 0 0 1 1054 1482"/>
  </g>
  <g fill="none" stroke="var(--gold)" stroke-width="2" stroke-linecap="round" stroke-linejoin="round">
    <!-- cloche -->
    <path d="M 240 1446 A 28 24 0 0 1 296 1446 Z M 234 1450 H 302 M 268 1420 V 1416 M 262 1416 H 274"/>
    <!-- scooter -->
    <circle cx="474" cy="1452" r="7"/><circle cx="506" cy="1452" r="7"/>
    <path d="M 481 1452 H 499 L 494 1436 H 482 M 474 1445 L 474 1438 H 484 M 496 1436 L 500 1424 H 506"/>
    <circle cx="486" cy="1422" r="7"/>
    <!-- chef -->
    <circle cx="712" cy="1432" r="9"/>
    <path d="M 702 1420 A 10 8 0 0 1 722 1420 M 694 1462 A 18 16 0 0 1 730 1462 M 696 1462 H 728"/>
    <!-- heart -->
    <path d="M 934 1462 C 914 1448 910 1436 918 1428 C 925 1422 932 1426 934 1432 C 936 1426 943 1422 950 1428 C 958 1436 954 1448 934 1462 Z"/>
    <path d="M 926 1444 Q 934 1450 942 1444"/>
  </g>
</svg>
<div class="step" style="left:168px;top:1494px"><h3>CHOSE YOUR MEALS</h3><p>Lorem ipsum dolor sit amet, consectetur adipiscing elit, sed do eiusmod tempoididunt ut labore et dolore magna aliquis ipsum suspendisse ultrices gravida.</p></div>
<div class="step" style="left:390px;top:1494px"><h3>WE COOK &amp; DELIVER</h3><p>Lorem ipsum dolor sit ameectetur adipiscing elit, sed dostempoididunt ut labore et dolore magna aliquis ipsum suspendisse</p></div>
<div class="step" style="left:612px;top:1494px"><h3>HEAT &amp; EAT</h3><p>Lorem ipsum dolor sit amet, consectetur adipiscing elit, sed do eiusmod tempoididunt ut labore et dolore magna aliquis ipsum suspendisse ultrices gravida.</p></div>
<div class="step" style="left:834px;top:1494px"><h3>ENJOY &amp; REPEAT</h3><p>Lorem ipsum dolor sit amet, consectetur adipiscing elit, sed do eiusmod tempoididunt ut labore et dolore magna aliquis ipsum suspendisse ultrices gravida.</p></div>

<a class="btn btn-gold" style="left:515px;top:1680px;width:170px;height:45px;font-size:14px">GET STARTED</a>

<!-- Members -->
<div class="section-title" style="top:1826px">OUR FAMOUS MEMBERS</div>
<div class="rule" style="left:576px;top:1885px"></div>

<svg class="layer" aria-hidden="true">
  <path d="M 84 2058 L 54 2088 L 84 2118 M 1116 2058 L 1146 2088 L 1116 2118" fill="none" stroke="#bbb" stroke-width="2"/>
</svg>
<div class="member" style="left:153px;top:1946px"><div class="name"><i></i>Orlo.</div><p>Lorem ipsum dolor sit amet,<br>consectetur adipiscing elit,<br>sed do eiusmod tempor</p></div>
<div class="member featured" style="left:457px;top:1946px"><div class="name"><i></i>Mivan.</div><p>Lorem ipsum dolor sit amet,<br>consectetur adipiscing elit,<br>sed do eiusmod tempor</p></div>
<div class="member" style="left:762px;top:1946px"><div class="name"><i></i>Rondo</div><p>Lorem ipsum dolor sit amet,<br>consectetur adipiscing elit,<br>sed do eiusmod tempor</p></div>
<div class="abs badge-sales">AVERAGE<br>+ 15%<br>SALES</div>

<!-- Call to action -->
<div class="abs cta-copy">Lorem ipsum dolor sit amet, consectetur adipiscing elit, sed do eiusmod tempor incididunt ut labore et dolore magna aliqua.</div>
<div class="sales-bar" style="left:121px;top:2453px;width:588px;height:78px">
  <span class="label" style="margin-left:30px">AVERAGE 15% ONLINE SALES</span>
</div>
<a class="btn btn-gold-text" style="left:528px;top:2470px;width:158px;height:44px">Subscribe Now</a>

<div class="photo" style="left:836px;top:2323px;width:246px;height:246px;border:6px solid var(--gold);background:radial-gradient(circle at 45% 40%,#e6ddd0,#b8a184 60%,#6f5c48)" role="img" aria-label="Smiling woman holding a phone and a paper grocery bag"></div>
<div class="photo" style="left:990px;top:2478px;width:92px;height:92px;background:var(--black);border:4px solid var(--gold)"></div>

<!-- Newsletter -->
<svg class="layer" aria-hidden="true">
  <polygon points="0,2890 455,2631 1200,2858 1200,3220 0,3220" fill="#1c1c1c"/>
  <polygon points="0,2900 455,2664 1200,2876 1200,3220 0,3220" fill="var(--gold-deep)"/>
</svg>
<div class="abs brand" style="left:560px;top:2778px;width:80px">
  <span class="dot" style="width:52px;height:52px;border-color:var(--gold-soft)"></span>
</div>
<div class="abs news-title">SUBSCRIBE TO<br>OUR NEWSLETTER</div>
<div class="abs news-copy">Lorem ipsum dolor sit amet, consectetur adipiscing elit, sed do eiusmod</div>
<div class="abs email">Enter Email</div>
<div class="abs subscribe">SUBSCRIBE</div>

<!-- Footer -->
<div class="abs brand" style="left:148px;top:3312px;width:200px;font-size:20px;letter-spacing:1.5px">
  <span class="dot" style="width:58px;height:58px;margin-bottom:14px"></span>GILDED PLATE<br><span style="font-size:17px">SEAL</span>
</div>
<div class="foot-divider" style="left:387px"></div>
<div class="foot-divider" style="left:614px"></div>
<div class="foot-divider" style="left:847px"></div>
<div class="foot-col" style="left:438px"><h4>QUICK LINKS</h4><a>Home</a><a>Who we are</a><a>How it works</a><a>Our Partners</a></div>
<div class="foot-col" style="left:665px"><h4>OTHER LINKS</h4><a>Terms and Conditions</a><a>Privacy policy</a><a>Sitemap</a><a>Information</a></div>
<div class="foot-col" style="left:901px"><h4>STAY CONNECTED</h4></div>
<div class="social" style="left:902px;top:3355px" role="img" aria-label="Social profile"></div>
<div class="social" style="left:975px;top:3355px" role="img" aria-label="Social profile"></div>
<div class="social" style="left:902px;top:3417px" role="img" aria-label="Social profile"></div>
<div class="social" style="left:975px;top:3417px" role="img" aria-label="Social profile"></div>

<div class="abs foot-line"></div>
<div class="abs copyright">© 2022 Gilded Plate Seal. All rights reserved.Privacy &nbsp;| &nbsp;Terms of Use</div>
<div class="store" style="left:840px" role="img" aria-label="App store download badge"></div>
<div class="store" style="left:957px" role="img" aria-label="App store download badge"></div>

</body>
</html>
```